New B2C website design to help dads be better dads

KinHarbor is a website to help dads be the “best dad you can be.”

We require our website to be designed into a PSD format, no coding necessary.

The general concept is a two-page design. The first page is the login page, the second page is the home page. Once at the home page, rather than navigating to and from different pages, the user will push and pull through different visual and functional layers of the hierarchy. In theory, this should add to the user experience by having a visual anchor of where they are (through layered pagination) as well as improving loading times since the new information should only be a delta in data load versus a brand new page load.

The general look-and-feel we are going for is clean, simple, minimal. This means that the winning design will show us a good eye for web-optimized typography, good use of white (negative) space, and good use of a visually pleasing grid.

We require a total of 6 page "views" plus the landing page. We note that many of the views are similar to one another.
Landing page
Milestone view
Task view
Content view, articles
Content view, products
Search view
What's new view

Please review all of the additional information provided as well as the attachments for examples.

We provide the following websites as good references for:

Typography:
http://quillbrenner.com/journal/

Use of white space:
http://www.dotlantern.com/
http://tidekiosk.com/

Example for “scrolling” page concept as well as good balance of color, typography, and white space:
http://www.morvensummit.eu/

Please contact us with questions so that we can guide your design effort.
Updates

Hello designers,

The following information is added to help guide the design process:

1.  For the text dialogue below the landing page, please assume the following word count:
"why are we making kin harbor?": 250 words
"who are we?" 200 words
"what's the deal with the penguin logo?" 300 words

For the social media links, please see http://www.glowberrycritics.com/
Notice the floating "social" bar that is always to the right.  This is the concept we are going for, please try to implement this as you see fit. 

Reason: Final design requests have been sent out to finalist designers, want to give everyone time to do a good job.

Target Market(s)

Fathers of young children ages 0-6 years old.

Industry/Entity Type

Product

Font styles to use
Sans Serif

Requirements
Must have
• Clean lines, minimal design concept

Incorporation of our logo (see attached document)

Header content is static for all views after landing page, see example

This page WILL be responsive, please keep that in mind when designing
The timeline bar should be to the left, with the timeline bar’s “milestones” also being responsive.

Designer is free to suggest font types, but any fonts used must be royalty-free and web-optimized. We request a minimum number of font types as well as fonts that load relatively fast. We reinforce that visually appealing typography is a significant factor in the winning design choice.

While we are not expecting the winning design to include code, please keep in mind that the final implementation needs to be optimized for desktop, tablet, and mobile platforms.

If you are using stock photography that is not generated by you, please provide where/how we can obtain imagery, as well as price.

All custom graphics must be available in original formats; Photoshop/GIMP layered files for layout design, and vector formats for logos, icons and other graphical elements.

Please incorporate “Blue” into design elements as you see fit, as the RGB 67 74 169 Blue is the primary color used in our brand. The complement to this blue is 255 202 0, a brownish orange. Feel free to use this color as well, although please keep it to a lesser amount.

Background color is your choice, do not feel the need to use the grey.
Should not have
• Excessive graphical content such that it affects loading times

Excessive use of too many font types such that it affects loading times

```html
<!DOCTYPE html>
<html lang="en">
<head>
<meta charset="utf-8">
<title>KinHarbor – Home</title>
<link href="https://fonts.googleapis.com/css2?family=Open+Sans:wght@400;600;700;800&display=swap" rel="stylesheet">
<style>
:root{
  --brand-blue:#434aa9;
  --brand-gold:#ffca00;
  --star:#f0a81c;
  --star-off:#c9c9c9;
  --ink:#333;
  --ink-soft:#666;
  --panel:#e4e4e4;
  --line:#cfcfcf;
  --white:#fff;
  --photo-a:#6b5a48;
  --photo-b:#b79b7d;
  --stroller-a:#7d7a55;
  --stroller-b:#d9d6c2;
}
*{box-sizing:border-box;margin:0;padding:0}
html,body{width:1200px;height:3861px;overflow:hidden}
body{position:relative;background:var(--white);font-family:"Open Sans",Arial,sans-serif;color:var(--ink);font-size:12px;line-height:1.45}

/* header */
.site-header{position:absolute;left:0;top:0;width:1200px;height:126px;background:var(--white)}
.brand{position:absolute;left:14px;top:8px;width:120px;text-align:center}
.brand-dot{display:block;width:62px;height:62px;border-radius:50%;background:var(--brand-blue);margin:0 auto 6px}
.brand-name{font-size:15px;font-weight:700;color:var(--brand-blue)}
.welcome{position:absolute;left:193px;top:12px;font-size:31px;font-weight:800;color:#222;letter-spacing:-.5px}
.score{position:absolute;left:193px;top:78px;font-size:13px;color:#444}
.score b{color:var(--brand-blue)}
.search-field{position:absolute;left:434px;top:76px;width:300px;height:36px;border:1px solid #bbb;background:var(--white)}
.btn{position:absolute;height:36px;background:var(--brand-blue);color:var(--white);font-weight:700;font-size:13px;display:flex;align-items:center;justify-content:center;border-radius:3px}
.btn-search{left:746px;top:76px;width:116px}
.account{position:absolute;left:958px;top:84px;font-size:13px}
.btn-logout{left:1062px;top:76px;width:112px}

/* timeline */
.timeline{position:absolute;left:41px;top:126px;width:2px;height:3735px;background:var(--line)}
.marker{position:absolute;left:6px;width:72px;height:50px;background:var(--white);border:1px solid #bbb;border-radius:4px;text-align:center;z-index:2}
.marker b{display:block;font-size:20px;line-height:24px;margin-top:3px;color:#333}
.marker span{display:block;font-size:11px;line-height:12px;color:#666}
.marker::after{content:"";position:absolute;left:-1px;bottom:-9px;border-left:14px solid var(--brand-gold);border-bottom:9px solid transparent}

/* panels */
.panel{position:absolute;left:100px;width:1074px;background:var(--panel);border-radius:14px}
.panel-label{position:absolute;left:10px;top:34px;font-size:16px;color:#333;display:flex;align-items:center;gap:10px}
.plus{width:22px;height:22px;border-radius:50%;border:1px solid #888;background:var(--white);display:flex;align-items:center;justify-content:center;font-weight:700;font-size:15px;line-height:1;color:#555}

/* checklist */
.checklist{position:absolute;left:29px;width:270px;background:var(--white);padding:14px 16px}
.checklist h3{font-size:16px;line-height:1.25;color:var(--brand-blue);font-weight:700;margin-bottom:10px}
.checklist li{list-style:none;display:flex;align-items:center;gap:14px;font-size:13.5px;height:33px}
.box{width:18px;height:18px;border:1px solid #aaa;background:#fafafa;flex:none;position:relative}
.box svg{position:absolute;left:1px;top:0}

.rating-block{position:absolute;left:29px;width:270px;font-size:12px}
.rating-block p{margin-top:8px;color:#444}

/* stars */
.stars{color:var(--star);letter-spacing:1px;font-size:15px}
.stars i{font-style:normal;color:var(--star-off)}

/* photo placeholders */
.photo{background:linear-gradient(135deg,var(--photo-a),var(--photo-b))}
.photo.stroller{background:linear-gradient(135deg,var(--stroller-b),var(--stroller-a) 60%,var(--stroller-b))}

/* cards */
.cards{position:absolute;left:328px;display:grid;grid-template-columns:250px 250px;column-gap:36px;row-gap:46px}
.card{background:var(--white);height:306px}
.card .photo{height:146px;margin:0}
.card-body{padding:10px 10px 0}
.kind{font-weight:700;color:var(--brand-blue);font-size:13px;letter-spacing:.3px}
.meta{display:flex;justify-content:space-between;align-items:center;margin:2px 0 6px;font-size:12px;color:#444}
.card p{font-size:12px;color:#333}

.sort{position:absolute;left:913px;font-size:13px}
.select{margin-top:4px;width:112px;height:26px;border:1px solid #aaa;background:var(--white);font-size:11px;padding:4px 6px;position:relative}
.select::after{content:"";position:absolute;right:7px;top:10px;border-left:5px solid transparent;border-right:5px solid transparent;border-top:6px solid #555}

/* detail views */
.detail-title{position:absolute;left:325px;top:30px;font-size:27px;color:#222}
.detail-rating{position:absolute;right:50px;top:38px;display:flex;gap:10px;align-items:center;font-size:13px}
.article-box{position:absolute;left:318px;top:74px;width:708px;height:305px;background:var(--white);padding:22px}
.article-box .photo{float:left;width:235px;height:148px;margin-right:20px}
.article-box p{font-size:12.5px;margin-bottom:12px}
.product-box{position:absolute;left:318px;top:112px;width:412px;height:428px;background:var(--white);padding:16px;font-size:12.5px}
.product-box p{margin-bottom:12px}
.product-box a{color:var(--brand-blue);text-decoration:none}
.reviewer{font-weight:600;color:var(--brand-blue)}
.buy-box{position:absolute;left:749px;top:112px;width:277px;height:348px;background:var(--white);padding:14px 16px}
.buy-box h4{font-size:20px;font-weight:600;color:var(--brand-blue);margin-bottom:10px}
.price-row{display:flex;justify-content:space-between;font-size:12.5px;line-height:22px}
.price-row b{color:var(--brand-blue)}
.buy-box .photo{height:120px;margin:12px 0 8px}

.query{position:absolute;left:29px;top:78px;font-size:16px;font-weight:600}

/* share bar */
.share{position:absolute;left:1142px;top:208px;width:58px;background:var(--white);border:1px solid #ccc;border-right:0;border-radius:6px 0 0 6px;padding:8px 0;text-align:center;z-index:3}
.share span{font-size:11px;color:#555;display:block;margin-bottom:4px}
.share i{display:block;width:38px;height:38px;border-radius:50%;background:var(--brand-blue);margin:8px auto 0}
</style>
</head>
<body>

<header class="site-header">
  <div class="brand"><span class="brand-dot"></span><span class="brand-name">KinHarbor</span></div>
  <h1 class="welcome">Welcome Greg, what would you like to do today?</h1>
  <div class="score">Super Dad Score: <b>10,500</b></div>
  <div class="search-field"></div>
  <div class="btn btn-search">SEARCH</div>
  <div class="account">My account</div>
  <div class="btn btn-logout">LOGOUT</div>
</header>

<aside class="share"><span>Share</span><i></i><i></i><i></i><i></i></aside>

<div class="timeline"></div>

<!-- Milestone view -->
<div class="marker" style="top:156px"><b>0</b><span>mo</span></div>
<section class="panel" style="top:129px;height:852px">
  <div class="panel-label"><span class="plus">+</span>Prepare for the baby arrival</div>
  <ul class="checklist" style="top:112px">
    <li><span class="box"></span>Buy a crib</li>
    <li><span class="box"></span>As semble the crib</li>
    <li><span class="box"></span>Buy a stroller</li>
    <li><span class="box"><svg width="16" height="16" viewBox="0 0 16 16"><path d="M2 8l4 4 8-9" fill="none" stroke="#434aa9" stroke-width="2.6"/></svg></span>Buy a carseat</li>
    <li><span class="box"></span>Install a carseat</li>
    <li><span class="box"></span>Learn to change a diaper</li>
    <li><span class="box"></span>Learn to hold a baby</li>
    <li><span class="box"></span>Set a feeding schedule</li>
  </ul>
  <div class="cards" style="top:112px">
    <article class="card"><div class="photo" role="img" aria-label="Dad fitting a car seat in the back of a car"></div><div class="card-body"><div class="kind">ARTICLE</div><div class="meta"><span class="stars">★★★<i>★★</i></span><span>3,121 ratings</span></div><p>I went out to buy my first car seat and had to earn my PhD in car seats, Newtonian physics, and anti-stain technology...</p></div></article>
    <article class="card"><div class="photo stroller" role="img" aria-label="Olive green stroller with matching carrier"></div><div class="card-body"><div class="kind">PRODUCT</div><div class="meta"><span class="stars">★★★<i>★★</i></span><span>9,102 likes</span></div><p>The Trekline XT stroller is this year's hottest stroller, for more reasons than are obvious. What we particularly like about it is...</p></div></article>
    <article class="card"><div class="photo" role="img" aria-label="Baby strapped into a car seat"></div><div class="card-body"><div class="kind">ARTICLE</div><div class="meta"><span class="stars">★★★<i>★★</i></span><span>1,595 likes</span></div><p>I learned something new this week which made my penny-pinching side just giddy. Car seats double as airplane...</p></div></article>
    <article class="card"><div class="photo" role="img" aria-label="Child buckled in a car seat"></div><div class="card-body"><div class="kind">ARTICLE</div><div class="meta"><span class="stars">★★★<i>★★</i></span><span>9,007 likes</span></div><p>Don't forget your go-bag essentials! Camping gear aside, Trailfolk Outfitters has assembled a great kit to take...</p></div></article>
  </div>
  <div class="sort" style="top:48px">Sort by:<div class="select">Most recent</div></div>
</section>

<!-- Content view, article -->
<div class="marker" style="top:1024px"><b>1</b><span>mo</span></div>
<section class="panel" style="top:1004px;height:550px">
  <div class="panel-label"><span class="plus">+</span>Prepare for the baby arrival</div>
  <h2 class="detail-title">Just Call Me Dr. Car Seat</h2>
  <div class="detail-rating"><span class="stars">★★★<i>★★</i></span><span>3,121 likes</span></div>
  <ul class="checklist" style="top:74px">
    <li><span class="box"></span>Buy a crib</li>
    <li><span class="box"></span>As semble the crib</li>
    <li><span class="box"></span>Buy a stroller</li>
    <li><span class="box"><svg width="16" height="16" viewBox="0 0 16 16"><path d="M2 8l4 4 8-9" fill="none" stroke="#434aa9" stroke-width="2.6"/></svg></span>Buy a carseat</li>
    <li><span class="box"></span>Install a carseat</li>
    <li><span class="box"></span>Learn to change a diaper</li>
    <li><span class="box"></span>Learn to hold a baby</li>
    <li><span class="box"></span>Set a feeding schedule</li>
  </ul>
  <div class="rating-block" style="top:382px">Rate this : <span class="stars">★★★<i>★★</i></span><p><b>Comments:</b><br>Lorem ipsum dolor sit amet, consectetur adipisicing elit, sed do eiusmod tempor incididunt ut labore et dolore magna aliqua. Ut enim ad minim veniam.</p></div>
  <article class="article-box">
    <div class="photo" role="img" aria-label="Dad fitting a car seat in the back of a car"></div>
    <p>I went out to buy my first car seat and had to earn my PhD in car seats, Newtonian physics, and anti-stain technology. Lorem ipsum dolor sit amet, consectetur adipisicing elit, sed do eiusmod tempor incididunt ut labore et dolore magna aliqua. Ut enim ad minim veniam, quis nostrud exercitation ullamco laboris nisi ut aliquip ex ea commodo consequat.</p>
    <p>Lorem ipsum dolor sit amet, consectetur adipisicing elit, sed do eiusmod tempor incididunt ut labore et dolore magna aliqua. Ut enim ad minim veniam, quis nostrud exercitation ullamco laboris nisi ut aliquip ex ea commodo consequat. Duis aute irure dolor in reprehenderit in voluptate velit esse cillum dolore eu fugiat nulla pariatur. Excepteur sint occaecat cupidatat non proident, sunt in culpa qui officia deserunt mollit anim id est laborum.</p>
  </article>
</section>

<!-- Content view, product -->
<div class="marker" style="top:1621px"><b>2</b><span>mo</span></div>
<section class="panel" style="top:1599px;height:589px">
  <div class="panel-label"><span class="plus">+</span>Prepare for the baby arrival</div>
  <h2 class="detail-title">Trekline XT Stroller</h2>
  <ul class="checklist" style="top:112px">
    <li><span class="box"></span>Buy a crib</li>
    <li><span class="box"></span>As semble the crib</li>
    <li><span class="box"></span>Buy a stroller</li>
    <li><span class="box"><svg width="16" height="16" viewBox="0 0 16 16"><path d="M2 8l4 4 8-9" fill="none" stroke="#434aa9" stroke-width="2.6"/></svg></span>Buy a carseat</li>
    <li><span class="box"></span>Install a carseat</li>
    <li><span class="box"></span>Learn to change a diaper</li>
    <li><span class="box"></span>Learn to hold a baby</li>
    <li><span class="box"></span>Set a feeding schedule</li>
  </ul>
  <div class="rating-block" style="top:416px">Rate this : <span class="stars">★★★<i>★★</i></span><p><b>Comments:</b><br>Lorem ipsum dolor sit amet, consectetur adipisicing elit, sed do eiusmod tempor incididunt ut labore et dolore magna aliqua. Ut enim ad minim veniam.</p></div>
  <div class="product-box">
    <p>The Trekline XT stroller is this year's hottest stroller, for more reasons than are obvious. What we particularly like about it is...</p>
    <p><a href="#">Fellow Dad's Reviews:</a></p>
    <p><span class="reviewer">DadRanger095:</span><br>Lorem ipsum dolor sit amet, consectetur adipisicing elit, sed do eiusmod tempor incididunt ut labore et dolore magna aliqua.</p>
    <p><a href="#">152</a> other Dad's found this review helpful.</p>
    <p><span class="reviewer">DadRanger095:</span><br>Lorem ipsum dolor sit amet, consectetur adipisicing elit, sed do eiusmod tempor incididunt ut labore et dolore magna aliqua.</p>
    <p><a href="#">105</a> other Dad's found this review helpful.</p>
  </div>
  <div class="buy-box">
    <h4>Available at:</h4>
    <div class="price-row"><span>Cradlemart.com</span><b>$249.95</b></div>
    <div class="price-row"><span>Babyland Depot</span><b>$258.95</b></div>
    <div class="price-row"><span>Tiny Nest Co</span><b>$277.95</b></div>
    <div class="photo" role="img" aria-label="Baby sitting in the stroller"></div>
    <div class="meta"><span class="stars">★★★<i>★★</i></span><span>3,121 likes</span></div>
  </div>
</section>

<!-- What's new view -->
<div class="marker" style="top:2242px"><b>3</b><span>mo</span></div>
<section class="panel" style="top:2220px;height:804px">
  <div class="panel-label"><span class="plus">+</span>What's the latest?</div>
  <ul class="checklist" style="top:90px">
    <h3>Related milestones<br>and tasks include:</h3>
    <li><span class="box"></span>Buy a crib</li>
    <li><span class="box"></span>As semble the crib</li>
    <li><span class="box"></span>Buy a stroller</li>
    <li><span class="box"><svg width="16" height="16" viewBox="0 0 16 16"><path d="M2 8l4 4 8-9" fill="none" stroke="#434aa9" stroke-width="2.6"/></svg></span>Buy a carseat</li>
    <li><span class="box"></span>Install a carseat</li>
    <li><span class="box"></span>Learn to change a diaper</li>
    <li><span class="box"></span>Learn to hold a baby</li>
    <li><span class="box"></span>Set a feeding schedule</li>
  </ul>
  <div class="cards" style="top:90px">
    <article class="card"><div class="photo" role="img" aria-label="Dad fitting a car seat in the back of a car"></div><div class="card-body"><div class="kind">ARTICLE</div><div class="meta"><span class="stars">★★★<i>★★</i></span><span>3,121 ratings</span></div><p>I went out to buy my first car seat and had to earn my PhD in car seats, Newtonian physics, and anti-stain technology...</p></div></article>
    <article class="card"><div class="photo stroller" role="img" aria-label="Olive green stroller with matching carrier"></div><div class="card-body"><div class="kind">PRODUCT</div><div class="meta"><span class="stars">★★★<i>★★</i></span><span>9,102 likes</span></div><p>The Trekline XT stroller is this year's hottest stroller, for more reasons than are obvious. What we particularly like about it is...</p></div></article>
    <article class="card"><div class="photo" role="img" aria-label="Baby strapped into a car seat"></div><div class="card-body"><div class="kind">ARTICLE</div><div class="meta"><span class="stars">★★★<i>★★</i></span><span>1,595 likes</span></div><p>I learned something new this week which made my penny-pinching side just giddy. Car seats double as airplane...</p></div></article>
    <article class="card"><div class="photo" role="img" aria-label="Child buckled in a car seat"></div><div class="card-body"><div class="kind">ARTICLE</div><div class="meta"><span class="stars">★★★<i>★★</i></span><span>9,007 likes</span></div><p>Don't forget your go-bag essentials! Camping gear aside, Trailfolk Outfitters has assembled a great kit to take...</p></div></article>
  </div>
  <div class="sort" style="top:40px">Sort by:<div class="select">Most recent</div></div>
</section>

<!-- Search view -->
<div class="marker" style="top:3062px"><b>4</b><span>mo</span></div>
<section class="panel" style="top:3040px;height:788px">
  <div class="panel-label"><span class="plus">+</span>What you searched for:</div>
  <div class="query">Car seats</div>
  <ul class="checklist" style="top:118px">
    <h3>Milestones and tasks<br>related to your search:</h3>
    <li><span class="box"></span>Buy a crib</li>
    <li><span class="box"></span>As semble the crib</li>
    <li><span class="box"></span>Buy a stroller</li>
    <li><span class="box"><svg width="16" height="16" viewBox="0 0 16 16"><path d="M2 8l4 4 8-9" fill="none" stroke="#434aa9" stroke-width="2.6"/></svg></span>Buy a carseat</li>
    <li><span class="box"></span>Install a carseat</li>
    <li><span class="box"></span>Learn to change a diaper</li>
    <li><span class="box"></span>Learn to hold a baby</li>
    <li><span class="box"></span>Set a feeding schedule</li>
  </ul>
  <div class="cards" style="top:90px">
    <article class="card"><div class="photo" role="img" aria-label="Dad fitting a car seat in the back of a car"></div><div class="card-body"><div class="kind">ARTICLE</div><div class="meta"><span class="stars">★★★<i>★★</i></span><span>3,121 ratings</span></div><p>I went out to buy my first car seat and had to earn my PhD in car seats, Newtonian physics, and anti-stain technology...</p></div></article>
    <article class="card"><div class="photo stroller" role="img" aria-label="Olive green stroller with matching carrier"></div><div class="card-body"><div class="kind">PRODUCT</div><div class="meta"><span class="stars">★★★<i>★★</i></span><span>9,102 likes</span></div><p>The Trekline XT stroller is this year's hottest stroller, for more reasons than are obvious. What we particularly like about it is...</p></div></article>
    <article class="card"><div class="photo" role="img" aria-label="Baby strapped into a car seat"></div><div class="card-body"><div class="kind">ARTICLE</div><div class="meta"><span class="stars">★★★<i>★★</i></span><span>1,595 likes</span></div><p>I learned something new this week which made my penny-pinching side just giddy. Car seats double as airplane...</p></div></article>
    <article class="card"><div class="photo" role="img" aria-label="Child buckled in a car seat"></div><div class="card-body"><div class="kind">ARTICLE</div><div class="meta"><span class="stars">★★★<i>★★</i></span><span>9,007 likes</span></div><p>Don't forget your go-bag essentials! Camping gear aside, Trailfolk Outfitters has assembled a great kit to take...</p></div></article>
  </div>
  <div class="sort" style="top:40px">Sort by:<div class="select">Most recent</div></div>
</section>

</body>
</html>
```